New travel store signage for Kelvane Journeys to attract luxury travellers.

Hello,
We are looking to change the signage of our stores. The signage must include the following:
1. Kelvane Journeys Logo (attached)
2. The text...The Travel & Cruise Experts
3. Brand Colours ( Fb0196, 412266, d41d84 and ffffff)
Please note the signage design must be central and only cover two thirds of the store front. We have also attached an image of one of our new stores which might be helpful when preparing a mock up.

We are looking for a quick turnaround on this, making a decision within 48 hours.

Target Market(s)

Retail

Industry/Entity Type

Travel Agency

Font styles to use
Other font styles liked:
• Radley

Colors
E54698
E96AAD
F1A4CE
F9D9EA
FCEFF6
6B429C
8869AF
B7A5CE
E3DAEB
F3F0F8

Requirements
Must have
• Hello, We are looking to change the signage of our stores. The signage must include the following: 1. Kelvane Journeys Logo (attached) 2. The text...The Travel & Cruise Experts 3. Brand Colours ( Fb0196, 412266, d41d84 and ffffff) Please note the signage design must be central and only cover two thirds of the store front.
Should not have
• different colour or fonts. Gradient design.

```html
<!DOCTYPE html>
<html lang="en">
<head>
<meta charset="utf-8">
<title>Kelvane Journeys – Store Signage</title>
<link rel="stylesheet" href="https://fonts.googleapis.com/css2?family=Montserrat:wght@800&display=swap">
<style>
  :root {
    --canvas: #ffffff;
    --backdrop: #ecebef;
    --sign-navy: #2a2f6b;
    --sign-charcoal: #2e2d31;
    --logo-panel: #ffffff;
    --brand-plum: #412266;
    --brand-magenta: #d41d84;
    --text-white: #ffffff;
  }
  * { margin: 0; padding: 0; box-sizing: border-box; }
  html, body {
    width: 1200px;
    height: 804px;
    overflow: hidden;
    background: var(--canvas);
  }
  .signage-board {
    width: 1200px;
    height: 804px;
    display: grid;
    grid-template-columns: 1fr 1fr;
    grid-template-rows: 1fr 1fr;
    gap: 8px;
  }
  .variant {
    background: var(--backdrop);
    display: flex;
    align-items: center;
    justify-content: center;
  }
  .fascia {
    width: 520px;
    height: 124px;
    display: flex;
    align-items: center;
    justify-content: center;
    gap: 16px;
    padding: 0 24px;
  }
  .fascia--navy { background: var(--sign-navy); }
  .fascia--charcoal {
    background: var(--sign-charcoal);
    border: 6px solid #1f1e22;
    height: 150px;
  }
  .logo-panel {
    width: 150px;
    height: 88px;
    background: var(--logo-panel);
    display: flex;
    align-items: center;
    justify-content: center;
    flex-shrink: 0;
  }
  .logo-name {
    font-family: 'Montserrat', sans-serif;
    font-weight: 800;
    font-size: 14px;
    color: var(--brand-plum);
    text-align: center;
    line-height: 1.2;
  }
  .tagline {
    font-family: 'Montserrat', sans-serif;
    font-weight: 800;
    font-size: 29px;
    line-height: 1.12;
    text-transform: uppercase;
    letter-spacing: 0.3px;
  }
  .tagline--white { color: var(--text-white); }
  .tagline--magenta { color: var(--brand-magenta); }
</style>
</head>
<body>
  <main class="signage-board">
    <section class="variant">
      <div class="fascia fascia--navy">
        <div class="logo-panel"><span class="logo-name">Kelvane Journeys</span></div>
        <p class="tagline tagline--white">The Travel &amp;<br>Cruise Experts</p>
      </div>
    </section>
    <section class="variant">
      <div class="fascia fascia--navy">
        <div class="logo-panel"><span class="logo-name">Kelvane Journeys</span></div>
        <p class="tagline tagline--magenta">The Travel &amp;<br>Cruise Experts</p>
      </div>
    </section>
    <section class="variant">
      <div class="fascia fascia--charcoal">
        <div class="logo-panel"><span class="logo-name">Kelvane Journeys</span></div>
        <p class="tagline tagline--white">The Travel &amp;<br>Cruise Experts</p>
      </div>
    </section>
    <section class="variant">
      <div class="fascia fascia--charcoal">
        <div class="logo-panel"><span class="logo-name">Kelvane Journeys</span></div>
        <p class="tagline tagline--magenta">The Travel &amp;<br>Cruise Experts</p>
      </div>
    </section>
  </main>
</body>
</html>
```